business card deign

Logo needs the following on it.
1. attached logo
2. Tagline - "If it keeps a drink cold or the party going...we do it!"
3. Name- Delia Fenwick, Founder and CPO
4. Address - 418 E. Harlow Avenue, Ste 2204, Tampa, FL. 33719
5. Phone - 720.555.0187

```html
<!DOCTYPE html>
<html lang="en">
<head>
<meta charset="utf-8">
<title>Chillbay Business Card</title>
<link rel="stylesheet" href="https://fonts.googleapis.com/css2?family=Roboto+Condensed:wght@400;700&family=Roboto:wght@400&display=swap">
<style>
  :root {
    --backdrop: #6f6f70;
    --card-dark: #151515;
    --card-light: #ffffff;
    --ink: #111111;
    --ink-soft: #1f1f1f;
    --emboss: #2c2c2c;
    --tagline: #f2f2f2;
  }
  html, body {
    margin: 0;
    padding: 0;
    width: 900px;
    height: 1200px;
    overflow: hidden;
    background: var(--backdrop);
  }
  .canvas {
    position: relative;
    width: 900px;
    height: 1200px;
  }
  .card {
    position: absolute;
    box-sizing: border-box;
  }
  .card--front {
    left: 134px;
    top: 214px;
    width: 630px;
    height: 357px;
    background: var(--card-dark);
  }
  .card--back {
    left: 135px;
    top: 628px;
    width: 631px;
    height: 359px;
    background: var(--card-light);
  }
  .logo-symbol-area {
    position: absolute;
    border-radius: 4px;
  }
  .card--front .logo-symbol-area {
    left: 200px;
    top: 78px;
    width: 225px;
    height: 150px;
    background: linear-gradient(180deg, #2e2e2e, #1c1c1c);
  }
  .card--back .logo-symbol-area {
    left: 132px;
    top: 105px;
    width: 170px;
    height: 116px;
    background: #1a1a1a;
  }
  .wordmark {
    position: absolute;
    font-family: "Roboto Condensed", sans-serif;
    font-weight: 700;
    text-align: center;
    white-space: nowrap;
  }
  .card--front .wordmark {
    left: 0;
    width: 100%;
    top: 238px;
    font-size: 36px;
    letter-spacing: 16px;
    text-indent: 16px;
    color: var(--emboss);
  }
  .card--back .wordmark {
    left: 100px;
    width: 240px;
    top: 226px;
    font-size: 29px;
    letter-spacing: 10px;
    text-indent: 10px;
    color: var(--ink);
  }
  .tagline {
    position: absolute;
    left: 0;
    width: 100%;
    top: 304px;
    text-align: center;
    font-family: "Roboto Condensed", sans-serif;
    font-size: 15.5px;
    letter-spacing: 0.8px;
    color: var(--tagline);
  }
  .divider {
    position: absolute;
    left: 340px;
    top: 97px;
    width: 2px;
    height: 164px;
    background: var(--ink);
  }
  .contact {
    position: absolute;
    left: 367px;
    top: 106px;
    color: var(--ink-soft);
    font-family: "Roboto", Arial, sans-serif;
  }
  .contact__name {
    margin: 0;
    font-family: "Roboto Condensed", sans-serif;
    font-weight: 700;
    font-size: 30px;
    line-height: 36px;
    color: var(--ink);
  }
  .contact__role {
    margin: 3px 0 0;
    font-size: 13.5px;
  }
  .contact__phone {
    margin: 12px 0 0;
    font-size: 16px;
    letter-spacing: 0.8px;
    display: flex;
    align-items: center;
    gap: 6px;
  }
  .contact__address {
    margin: 10px 0 0;
    font-size: 13.5px;
    line-height: 25px;
    font-style: normal;
  }
</style>
</head>
<body>
<main class="canvas">
  <section class="card card--front">
    <div class="logo-symbol-area" role="img" aria-label="Brand symbol area"></div>
    <div class="wordmark">CHILLBAY</div>
    <p class="tagline" style="margin:0">If it keeps a drink cold or the party going...we do it!</p>
  </section>

  <section class="card card--back">
    <div class="logo-symbol-area" role="img" aria-label="Brand symbol area"></div>
    <div class="wordmark">CHILLBAY</div>
    <div class="divider"></div>
    <div class="contact">
      <h1 class="contact__name">DELIA FENWICK</h1>
      <p class="contact__role">Founder and CPO</p>
      <p class="contact__phone">
        <svg width="12" height="12" viewBox="0 0 24 24" aria-hidden="true"><path fill="#111" d="M6.6 10.8a15.1 15.1 0 0 0 6.6 6.6l2.2-2.2c.3-.3.7-.4 1-.2 1.1.4 2.3.6 3.6.6.6 0 1 .4 1 1V20c0 .6-.4 1-1 1A17 17 0 0 1 3 4c0-.6.4-1 1-1h3.5c.6 0 1 .4 1 1 0 1.3.2 2.5.6 3.6.1.3 0 .7-.2 1z"/></svg>
        720.555.0187
      </p>
      <address class="contact__address">418 E. Harlow Avenue, Ste 2204<br>Tampa, FL. 33719</address>
    </div>
  </section>
</main>
</body>
</html>
```